Need Business Cards Created

We just started a new fitness holdings company that will own, create, and manage mobile fitness apps. We have just created a logo and we now need professional business cards created. Need a professional yet somewhat sporty look. DO NOT WANT ANY CHANGES TO OUR LOGO. Would like to keep the same color scheme. We have two logo versions you can choose from or you can submit a double proposal using each logo variation.

PLEASE DO NOT SUBMIT ANY GENERIC TEMPLATES AS YOUR ENTRY WILL NOT BE CONSIDERED. WILL ONLY TAKE CUSTOMIZED PROPOSALS THAT FOLLOW THE REQUIREMENTS.

```html
<!DOCTYPE html>
<html lang="en">
<head>
<meta charset="utf-8">
<title>Kinetra — Business Card</title>
<link rel="stylesheet" href="https://fonts.googleapis.com/css2?family=Arimo:wght@400;700&display=swap">
<style>
  :root {
    --stage: #e9ecef;
    --card-white: #ffffff;
    --navy: #123448;
    --navy-deep: #0c2738;
    --brand-blue: #1e8fd6;
    --ink: #1f2a33;
    --ink-soft: #4a5560;
  }
  * { box-sizing: border-box; margin: 0; padding: 0; }
  html, body {
    width: 1200px; height: 900px; overflow: hidden;
    background: var(--stage);
    font-family: "Arimo", Arial, sans-serif;
  }
  .stage {
    position: relative; width: 1200px; height: 900px;
    display: flex; flex-direction: column; align-items: center; justify-content: center; gap: 60px;
  }
  .card {
    position: relative; width: 560px; height: 320px;
    border-radius: 22px; overflow: hidden;
    box-shadow: 0 10px 30px rgba(0,0,0,0.18);
  }
  /* Front */
  .card-front { background: var(--card-white); color: var(--ink); }
  .brand {
    position: absolute; left: 40px; top: 42px;
    display: flex; align-items: center; gap: 10px;
  }
  .brand-dot { width: 22px; height: 22px; border-radius: 50%; background: var(--brand-blue); }
  .brand-name { font-weight: 700; font-size: 30px; letter-spacing: 1px; color: var(--navy); }
  .contact {
    position: absolute; left: 40px; top: 130px;
    font-size: 14px; line-height: 22px; color: var(--ink-soft);
  }
  .contact-line { display: flex; align-items: center; gap: 8px; }
  .contact-line.plain { padding-left: 0; }
  .contact-icon { width: 12px; height: 12px; flex: none; }
  .person {
    position: absolute; right: 40px; top: 120px; text-align: right;
  }
  .person-name { font-size: 20px; letter-spacing: 0.5px; text-transform: uppercase; color: var(--ink); }
  .person-name .surname { color: var(--brand-blue); }
  .person-role { font-size: 14px; color: var(--ink-soft); margin-top: 4px; }
  .edge-tab {
    position: absolute; right: 0; top: 126px;
    width: 8px; height: 26px; background: var(--brand-blue);
    border-radius: 4px 0 0 4px;
  }
  .website {
    position: absolute; right: 40px; bottom: 30px;
    font-size: 14px; color: var(--ink-soft);
  }
  .bottom-tab {
    position: absolute; bottom: 0; left: 210px;
    width: 110px; height: 8px; background: var(--navy);
    border-radius: 6px 6px 0 0;
  }
  /* Back */
  .card-back { background: var(--navy); }
  .back-pattern {
    position: absolute; inset: 0;
    background: linear-gradient(135deg, var(--navy) 0%, var(--navy-deep) 100%);
  }
  .back-brand {
    position: absolute; inset: 0;
    display: flex; align-items: center; justify-content: center; gap: 12px;
  }
  .back-brand .brand-dot { width: 26px; height: 26px; }
  .back-brand .brand-name { color: var(--brand-blue); font-size: 36px; }
</style>
</head>
<body>
<main class="stage">
  <section class="card card-front">
    <div class="brand">
      <span class="brand-dot"></span>
      <span class="brand-name">KINETRA</span>
    </div>
    <div class="contact">
      <div class="contact-line">4820 W. Summit Ave.</div>
      <div class="contact-line">Mesa Ridge, CO 80512</div>
      <div class="contact-line">
        <svg class="contact-icon" viewBox="0 0 24 24"><path fill="#1e8fd6" d="M6.6 10.8a15.1 15.1 0 0 0 6.6 6.6l2.2-2.2a1 1 0 0 1 1-.25 11.4 11.4 0 0 0 3.6.57 1 1 0 0 1 1 1V20a1 1 0 0 1-1 1A17 17 0 0 1 3 4a1 1 0 0 1 1-1h3.5a1 1 0 0 1 1 1c0 1.25.2 2.45.57 3.6a1 1 0 0 1-.25 1z"/></svg>
        +100 55 010 020
      </div>
      <div class="contact-line">
        <svg class="contact-icon" viewBox="0 0 24 24"><rect x="2" y="5" width="20" height="14" rx="2" fill="#1e8fd6"/><path d="M3 6l9 7 9-7" fill="none" stroke="#ffffff" stroke-width="2"/></svg>
        hello@kinetra.com
      </div>
    </div>
    <div class="person">
      <div class="person-name">Dalton <span class="surname">Reyes</span></div>
      <div class="person-role">Director</div>
    </div>
    <span class="edge-tab"></span>
    <div class="website">www.kinetra.com</div>
    <span class="bottom-tab"></span>
  </section>

  <section class="card card-back">
    <div class="back-pattern" role="img" aria-label="Tone-on-tone repeating brand mark pattern in navy"></div>
    <div class="back-brand">
      <span class="brand-dot"></span>
      <span class="brand-name">KINETRA</span>
    </div>
  </section>
</main>
</body>
</html>
```